Zumbly - New Payment App for Student

Zum-bly - A Payment App for student to make payment, track own expenses and practice good dietary habits. The App theme is Fun and excitement.
Target User: Secondary Student aged 13-18
Look and Feel: Fun, excitement and simple.
Screen 1
Login to the app using thumbprints or password
Screen 2
Display the balance
Wallet balance >>> go to screen 3 to display transaction history
Gamification balance - points + badges >>> go to screen 3
Button to make payment
Screen 2-1
Allow them to do payment
Click “Pay”
Display QR code
scanning by merchant
Payment made
Notification received
The transaction history will be shown up
Screen 2-2
Allow them to top up (alternatively to parent Top-up using credit card)
Click “Top Up”
Display QR code
Pass the cash to merchant
scanning by merchant
Payment made
Notification received
The new balance will be shown up
Screen 3
Display more details on transaction history
Payment history + gamification history (gain/redeem points)
E.g. 14 Nov Canteen purchase $5.40
- Banana +30 points
- Milk +10 points
Screen 4 (play a game to earn point)
Introduce some trivial games (while waiting in line at cafeteria or school store) to gain some points
Crosswords
Puzzle
Screen 5 (Display achievements)
Leaderboard
Where the individual stands in the class
Where the class stands overall in school
Badges
Level
Achievements
For more, please go to our website http://www.zumbly-pay.example/
Target Market(s)
Secondary School Student aged 13-18
Industry/Entity Type
Education
Logo Text
zumbly
Look and feel

```html
<!DOCTYPE html>
<html lang="en">
<head>
<meta charset="utf-8">
<title>Zumbly – Sign in</title>
<link rel="stylesheet" href="https://fonts.googleapis.com/css2?family=Lilita+One&family=Fredoka:wght@500;600&display=swap">
<style>
  :root {
    --bg-orange: #f39a1e;
    --bg-orange-light: #fbb533;
    --bg-orange-deep: #e8741a;
    --band-orange: #ee6a16;
    --band-orange-dark: #d9520f;
    --frame-orange: #e67a1c;
    --frame-edge: #c85a10;
    --panel-yellow: #f7d21f;
    --panel-yellow-deep: #eeb416;
    --ribbon-pink: #ee5a8c;
    --ribbon-pink-dark: #c93a6c;
    --field-yellow: #f9f21e;
    --field-text: #3a7aa0;
    --ok-green: #8fd21e;
    --ok-green-dark: #5ea20c;
    --white: #ffffff;
  }
  * { box-sizing: border-box; margin: 0; padding: 0; }
  html, body { width: 1200px; height: 800px; overflow: hidden; }
  body {
    position: relative;
    font-family: "Lilita One", "Fredoka", sans-serif;
    background: radial-gradient(circle at 22% 18%, var(--bg-orange-light) 0%, var(--bg-orange) 45%, var(--bg-orange-deep) 100%);
  }
  .base-band {
    position: absolute;
    left: 520px; top: 330px; width: 720px; height: 520px;
    border-radius: 80px 0 0 0;
    background: linear-gradient(180deg, var(--band-orange) 0%, var(--band-orange-dark) 100%);
  }
  .app-name {
    position: absolute; left: 64px; top: 52px;
    font-family: "Fredoka", sans-serif;
    font-weight: 600;
    font-size: 44px; line-height: 1;
    color: var(--white);
  }
  .panel {
    position: absolute;
    border-radius: 46px;
    background: var(--frame-orange);
    border: 4px solid var(--frame-edge);
    padding: 22px;
    box-shadow: 0 14px 0 rgba(160,60,10,0.35);
  }
  .panel-face {
    width: 100%; height: 100%;
    border-radius: 32px;
    background: radial-gradient(circle at 50% 40%, var(--panel-yellow) 0%, var(--panel-yellow-deep) 100%);
    border: 4px solid var(--frame-edge);
    position: relative;
  }
  .panel-fingerprint { left: 190px; top: 150px; width: 440px; height: 330px; }
  .panel-login { left: 570px; top: 380px; width: 470px; height: 350px; }
  .ribbon {
    position: absolute; left: 50%; top: -52px;
    transform: translateX(-50%) rotate(-6deg);
    width: 270px; height: 56px;
  }
  .ribbon-band {
    position: absolute; inset: 0;
    background: var(--ribbon-pink);
    border-radius: 6px;
    display: flex; align-items: center; justify-content: center;
    color: var(--white); font-size: 26px;
    z-index: 1;
  }
  .ribbon-tail {
    position: absolute; top: 16px; width: 56px; height: 48px;
    background: var(--ribbon-pink-dark);
  }
  .ribbon-tail.left { left: -34px; clip-path: polygon(0 0, 100% 0, 100% 100%, 0 100%, 30% 50%); }
  .ribbon-tail.right { right: -34px; clip-path: polygon(0 0, 100% 0, 70% 50%, 100% 100%, 0 100%); }
  .fingerprint-icon {
    position: absolute; left: 50%; top: 54%;
    transform: translate(-50%, -50%);
    width: 120px; height: 120px; border-radius: 50%;
    background: radial-gradient(circle, var(--field-yellow) 0%, var(--panel-yellow-deep) 100%);
    border: 4px solid var(--frame-edge);
  }
  .login-form { position: absolute; left: 60px; top: 70px; width: 270px; }
  .field {
    height: 44px; margin-bottom: 22px;
    background: var(--field-yellow);
    border-radius: 8px;
    box-shadow: 0 4px 0 rgba(180,120,10,0.5);
    display: flex; align-items: center; padding: 0 16px;
    font-family: "Fredoka", sans-serif; font-weight: 600;
    font-size: 20px; color: var(--field-text);
  }
  .field-password { letter-spacing: 6px; }
  .ok-button {
    position: absolute; right: -40px; top: 50px;
    width: 76px; height: 76px; border-radius: 50%;
    background: radial-gradient(circle at 40% 35%, #b8ee4a 0%, var(--ok-green) 55%, var(--ok-green-dark) 100%);
    box-shadow: 0 5px 0 rgba(80,100,10,0.5);
    display: flex; align-items: center; justify-content: center;
    color: var(--field-yellow); font-size: 28px;
  }
</style>
</head>
<body>
  <div class="base-band"></div>

  <div class="app-name">Zumbly</div>

  <section class="panel panel-fingerprint">
    <div class="panel-face">
      <div class="ribbon">
        <span class="ribbon-tail left"></span>
        <span class="ribbon-tail right"></span>
        <div class="ribbon-band">Finger Print</div>
      </div>
      <div class="fingerprint-icon" role="img" aria-label="Fingerprint scanner graphic"></div>
    </div>
  </section>

  <section class="panel panel-login">
    <div class="panel-face">
      <div class="ribbon">
        <span class="ribbon-tail left"></span>
        <span class="ribbon-tail right"></span>
        <div class="ribbon-band">Login</div>
      </div>
      <div class="login-form">
        <div class="field field-username">user name</div>
        <div class="field field-password">●●●●●</div>
      </div>
    </div>
    <div class="ok-button">OK</div>
  </section>
</body>
</html>
```